Bussines Card - TR EDIFICACIONES, S.A.

We need a design for a business card.
I want it to look professional, but not old fashion.
We are like "young people', somehow i want it to look fresh, new, different, but still serious and professional.
I could use, a non typical design. (I mean, not just rectangular design).

The company Name is " TR EDIFICACIONES, S.A. " we are Panamenian company (spanish language) dedicated to construction and civil engeniering.

The company logo is attached, i use it with white background. Im not sure trying different one, could try.

Industry/Entity Type

Business

```html
<!DOCTYPE html>
<html lang="es">
<head>
<meta charset="utf-8">
<title>TR Edificaciones – Tarjeta de presentación</title>
<link rel="stylesheet" href="https://fonts.googleapis.com/css2?family=PT+Sans+Narrow:wght@400;700&display=swap">
<style>
  :root {
    --backdrop: #2b2b2b;
    --card: #ffffff;
    --ink: #5f5f5f;
    --ink-dark: #3c3c3c;
    --rule: #c9c9c9;
  }
  * { margin: 0; padding: 0; box-sizing: border-box; }
  html, body { width: 1200px; height: 675px; overflow: hidden; }
  body {
    background: var(--backdrop);
    font-family: "PT Sans Narrow", "Arial Narrow", sans-serif;
    color: var(--ink);
    display: flex;
    align-items: center;
    justify-content: center;
    gap: 60px;
  }
  .card {
    width: 525px;
    height: 300px;
    background: var(--card);
    position: relative;
  }

  /* Contact side */
  .card--contact .brand {
    position: absolute;
    left: 44px;
    top: 40px;
  }
  .brand-mark {
    width: 86px;
    height: 86px;
    background: var(--ink);
    display: block;
  }
  .brand-name {
    margin-top: 8px;
    font-weight: 700;
    font-size: 13px;
    letter-spacing: 1px;
    color: var(--ink);
  }
  .person-name {
    margin-top: 6px;
    font-weight: 700;
    font-size: 17px;
    color: var(--ink-dark);
    letter-spacing: 0.5px;
  }
  .person-title {
    font-weight: 700;
    font-size: 10px;
    letter-spacing: 0.8px;
    color: var(--ink);
  }
  .contact {
    position: absolute;
    left: 250px;
    top: 140px;
    padding-left: 20px;
    border-left: 1px solid var(--rule);
    font-size: 12px;
    line-height: 1.45;
    letter-spacing: 0.4px;
    text-transform: uppercase;
  }
  .contact-address { margin-bottom: 12px; }
  .contact-line { display: flex; align-items: center; gap: 8px; }
  .contact-line svg { width: 10px; height: 10px; fill: var(--ink); flex: none; }

  /* Brand side */
  .card--brand {
    display: flex;
    flex-direction: column;
    align-items: center;
    justify-content: center;
  }
  .card--brand .brand-mark {
    width: 120px;
    height: 120px;
  }
  .card--brand .company {
    margin-top: 28px;
    font-weight: 700;
    font-size: 30px;
    letter-spacing: 4px;
    color: var(--ink);
  }
</style>
</head>
<body>
  <section class="card card--contact">
    <div class="brand">
      <span class="brand-mark"></span>
      <p class="brand-name">TR EDIFICACIONES</p>
      <p class="person-name">MARCO RÍOS</p>
      <p class="person-title">PRESIDENT &amp; CEO</p>
    </div>
    <div class="contact">
      <p class="contact-address">Calle 50, Bella Vista, Plaza Lumen,<br>2do piso local 4</p>
      <p class="contact-line">
        <svg viewBox="0 0 10 10" aria-hidden="true"><path d="M1 3 Q5 0 9 3 L8 4 L6.5 3.2 L6.5 4 L3.5 4 L3.5 3.2 L2 4 Z M2 5 H8 V9 H2 Z"/></svg>
        507-3810
      </p>
      <p class="contact-line">
        <svg viewBox="0 0 10 10" aria-hidden="true"><path d="M2.5 0 H7.5 V10 H2.5 Z M3.5 1 V8 H6.5 V1 Z"/></svg>
        507-6214-3390
      </p>
      <p class="contact-line">
        <svg viewBox="0 0 10 10" aria-hidden="true"><path d="M0 2 H10 V8 H0 Z M0.8 2.6 L5 5.6 L9.2 2.6 Z"/></svg>
        marco@tredifica.com
      </p>
      <p class="contact-line">
        <svg viewBox="0 0 10 10" aria-hidden="true"><circle cx="5" cy="5" r="4.2" fill="none" stroke="#5f5f5f" stroke-width="1.2"/><path d="M0.8 5 H9.2 M5 0.8 V9.2" stroke="#5f5f5f" stroke-width="0.8"/></svg>
        www.tredifica.com
      </p>
    </div>
  </section>

  <section class="card card--brand">
    <span class="brand-mark"></span>
    <h1 class="company">TR EDIFICACIONES</h1>
  </section>
</body>
</html>
```